Most captivating card ever!

Life Coach - Professional Adventurer - Entrepreneur
I need the worlds most amazing business card for my personal brand. This business card will mostly be used to give to prospective clients for life coaching and business coaching.
Be creative, be adventurous. It needs to stand out. Make people say.. I need this guy!
My background is as an entrepreneur and professional adventurer undertaking extreme expeditions. I am now moving into life coaching.
No specific design ideas, so you have full creativity. Show me your best.
Industry/Entity Type
Life Coaching
Contact Information for Business Card
Dan Pellow
itsdanp.com.au
0468215903
Colors
Designer to choose colors to be used in the design.
Look and feel

```html
<!DOCTYPE html>
<html lang="en">
<head>
<meta charset="UTF-8">
<title>Dan Pellow — Business Card</title>
<link rel="stylesheet" href="https://fonts.googleapis.com/css2?family=Oswald:wght@500&family=Work+Sans:wght@400&display=swap">
<style>
  :root {
    --backdrop: #e4e4e4;
    --card: #ffffff;
    --ink: #2b2b2b;
    --ink-soft: #333333;
  }
  html, body {
    margin: 0;
    padding: 0;
    width: 1200px;
    height: 898px;
    overflow: hidden;
    background: var(--backdrop);
  }
  .stage {
    width: 1200px;
    height: 898px;
    display: flex;
    align-items: center;
    justify-content: center;
  }
  .card {
    position: relative;
    width: 840px;
    height: 480px;
    background: var(--card);
    box-shadow: 0 6px 24px rgba(0,0,0,0.12);
    color: var(--ink);
  }
  .identity {
    position: absolute;
    left: 150px;
    top: 170px;
    display: flex;
    align-items: center;
    gap: 34px;
  }
  .name {
    font-family: "Oswald", sans-serif;
    font-weight: 500;
    font-size: 40px;
    letter-spacing: 2px;
    text-transform: uppercase;
    margin: 0;
    line-height: 1;
    padding-top: 40px;
  }
  .divider {
    width: 3px;
    height: 48px;
    background: var(--ink);
    align-self: flex-start;
    margin-top: 8px;
  }
  .contact {
    list-style: none;
    margin: 0;
    padding: 0;
    align-self: flex-start;
    font-family: "Work Sans", sans-serif;
    font-size: 19px;
    letter-spacing: 1px;
    color: var(--ink-soft);
  }
  .contact li {
    display: flex;
    align-items: center;
    gap: 14px;
    line-height: 28px;
  }
  .contact svg {
    width: 16px;
    height: 16px;
    fill: var(--ink);
  }
  .tagline {
    position: absolute;
    left: 200px;
    bottom: 78px;
    margin: 0;
    font-family: "Work Sans", sans-serif;
    font-size: 22px;
    letter-spacing: 1.5px;
    color: var(--ink-soft);
  }
</style>
</head>
<body>
  <main class="stage">
    <section class="card" aria-label="Business card for Dan Pellow">
      <div class="identity">
        <h1 class="name">Dan Pellow</h1>
        <span class="divider" aria-hidden="true"></span>
        <ul class="contact">
          <li>
            <svg viewBox="0 0 16 16" aria-hidden="true"><path d="M4.2 1.5c.4-.3.9-.2 1.2.2l1.6 2.4c.3.4.2.9-.1 1.2l-1.1 1c.6 1.5 1.8 2.8 3.4 3.6l1-1.1c.3-.3.8-.4 1.2-.1l2.4 1.5c.4.3.5.8.2 1.2l-1.1 1.6c-.4.5-1 .8-1.6.6C6.9 12.6 3.4 9 2.3 4.6c-.2-.6.1-1.2.6-1.6z"/></svg>
            <span>0468215903</span>
          </li>
          <li>
            <svg viewBox="0 0 16 16" aria-hidden="true"><path d="M1 3.5h14v1.2L8 9 1 4.7zM1 6.2l7 4.3 7-4.3v6.3H1z"/></svg>
            <span>itsdanp.com.au</span>
          </li>
        </ul>
      </div>
      <p class="tagline">Life Coach - Professional Adventurer - Entrepreneur</p>
    </section>
  </main>
</body>
</html>
```